Cloud-based Health 2.0 Web Site

We need the overall look and feel for a new cloud-based Health 2.0 web site where health professionals can manage and interact with their patients/clients.

The plan is to generate a landing page that can grab the attention of health professionals (doctors, nurses, personal trainers, etc...). This page should have an attractive "Sign Up for Free" or similar button/message, as well as a login section for users already registered. We currently have a view on having a number of messages displayed, either as a slider or as separate areas on the page (decision is up for grabs).

Secondly, we need a standard "framework" for all the other pages which will be accessible once the user has authenticated with a clean, airy and spacious feel. This will provide styling for standard elements (input boxes, checkboxes, etc...) as well as a given layout, possibly 3 columns (fixed-fluid-fixed) although we leave this to the designer's choice.

We want to stress the importance of the Cloud, as well as make users feel like "this is the place to be if you're a modern, tech savvy health professional". Also of high importance is to show that this is a secure place, where data is accessible from anywhere yet also highly protected.

This project is going to provide long-term work for the winner and possibly those we consider close runner ups, so if you guys are interested in grabbing our attention so you can become our designer of choice, this is your chance!

Standard pages we are looking to receive after the selection process:

* Landing page
* Health Professional Profile Page (personal details, professional details, photo...)
* Patient list / Patient Management page
* Patient profile (details, health details...)
* Generic "item" management page (item refers to documents, images, contacts, etc...)

The logo for the site/product is also up for grabs, and a bonus payment can be given if you provide one that both matches the style of the site whilst being one that could be reused for mobile app icons, etc...
Updates

The site name is "vitorbis" (all lower-case) for those of you wanting to work on the logo part. As I said before, the logo should contain a component that could be use as the recognisable icon in a mobile phone app. Something that can be easily identified in both the site and the app that connects them together.

vitorbis is made up of two parts (vitor + bis), and you might want to consider differentiating them by the use of colour, fonts or however you think appropriate.

New sample screen-shots of the existing functionality have been uploaded to help you mock up some screens.

PLEASE NOTE: This are to be used for content/widget design only! The layout of how these are represented, e.g. accordion, slider, tree, list... is entirely up to you! Don't guide your layout based on these screen-shots, unless you think they are the way to go, of course. 

We want your creative input, so please innovate! :)

Thanks!

Target Market(s)

Health Professionals

Industry/Entity Type

Health

Requirements
Must have
• * A landing page that grabs the users attention but is "different" from the rest of pages (although within the same design/style parameters)

* A generic page framework for the rest of the pages (style guide)
Nice to have
• A modern and clean logo to go with the site. If the logo is selected, this can result in a bonus payment to be decided.

```html
<!DOCTYPE html>
<html lang="en">
<head>
<meta charset="utf-8">
<title>Vitor Bis – Health platform in the cloud</title>
<link rel="stylesheet" href="https://fonts.googleapis.com/css2?family=Arimo:wght@400;700&family=PT+Sans:wght@400;700&family=Ubuntu:wght@400;500&display=swap">
<style>
:root{
  --header-bg:#efefef;
  --brand-blue:#1e9ad6;
  --ink:#555555;
  --ink-soft:#6b6b6b;
  --nav-dark:#1f1f1f;
  --lime:#b8d630;
  --lime-text:#d8ee3c;
  --welcome-green:#6a9e14;
  --heading-blue:#1a8ccc;
  --footer-bg:#262626;
  --footer-text:#cfcfcf;
  --white:#ffffff;
}
*{margin:0;padding:0;box-sizing:border-box}
html,body{width:1145px;height:1200px;overflow:hidden;background:var(--white)}
body{font-family:"Arimo",Arial,sans-serif;color:var(--ink)}
.page{position:absolute;left:0;top:0;width:1050px;height:1100px;transform:scale(1.0905,1.0909);transform-origin:0 0}
.abs{position:absolute}

/* header */
.site-header{left:0;top:0;width:1050px;height:94px;background:var(--header-bg)}
.brand{left:48px;top:16px;display:flex;align-items:center;gap:14px}
.brand-mark{width:54px;height:54px;border-radius:50%;background:#8fb8cf}
.brand-name{font-size:48px;color:var(--ink);font-weight:400;letter-spacing:-.5px}
.main-nav{left:563px;top:20px;width:398px;height:46px;border-radius:23px;background:linear-gradient(#333,#151515);display:flex;align-items:center;padding-left:12px}
.main-nav a{color:#fff;text-decoration:none;font-size:15px;padding:0 20px;height:46px;line-height:46px;border-right:1px solid #3d3d3d}
.main-nav a:last-child{border-right:0}
.main-nav a.current{color:var(--lime);position:relative}
.nav-marker{left:596px;top:16px}

/* hero */
.hero{left:0;top:97px;width:1050px;height:430px;background:radial-gradient(ellipse at 35% 30%,#39aee4 0%,var(--brand-blue) 55%,#1b8fcb 100%)}
.hero-sweep{left:0;top:97px}
.hero-pitch{left:60px;top:161px;width:428px;font-size:20px;line-height:30px;color:#fff;text-align:justify}
.hero-pitch a{color:var(--lime-text);font-size:16px;text-decoration:none;margin-left:6px}
.btn{border-radius:6px;font-family:"Ubuntu",sans-serif;font-size:19px;display:flex;align-items:center;justify-content:center;height:46px}
.btn-signup{left:207px;top:316px;width:160px;background:linear-gradient(#c4ee3a,#7cc80c);border:1px solid #d6f56b;color:#2e5206}
.btn-login{left:398px;top:316px;width:90px;background:linear-gradient(#f6a81e,#e07b05);border:1px solid #f7c45c;color:#5a2c00}
.hero-tagline{left:60px;top:381px;width:440px;font-size:16px;line-height:24px;color:#fff}
.photo-frame{left:518px;top:119px;width:485px;height:324px;background:#fff;box-shadow:0 6px 14px rgba(0,0,0,.18)}
.photo-slot{left:528px;top:129px;width:465px;height:305px;background:linear-gradient(90deg,#e4e4e2,#f4f4f2 50%,#e8e8e6);border:1px solid #d8d8d8}
.slider-controls{left:625px;top:461px;width:271px;height:43px;border-radius:10px;background:rgba(255,255,255,.28);display:flex;align-items:center;justify-content:center;gap:10px;font-size:15px;color:#111}
.dot{width:11px;height:11px;border-radius:50%;border:2px solid #111;background:#fff}
.dot.active{background:var(--lime)}

/* welcome */
.welcome{left:30px;top:527px;width:990px;height:136px;background:radial-gradient(ellipse at 50% 40%,#fff 60%,#f1f1f1 100%);border-bottom:1px solid #e8e8e8}
.welcome-title{left:76px;top:554px;font-size:20px;color:var(--welcome-green)}
.welcome-text{left:76px;top:587px;width:915px;font-size:16px;line-height:26px;color:var(--ink)}
.pill{display:inline-block;background:linear-gradient(#3a3a3a,#1a1a1a);border-radius:7px;font-size:12px;padding:3px 13px;vertical-align:middle}
.pill-green{color:#8dbf22;margin-left:6px}

/* columns */
.col{top:684px;width:252px}
.col h2{font-size:18px;font-weight:400;color:var(--heading-blue);height:34px;border-bottom:1px dashed #5a9ccc}
.thumb{width:88px;height:78px;border:1px solid #cfcfcf;float:left;margin-right:10px}
.body-copy{font-family:"PT Sans",sans-serif;font-size:11.5px;line-height:18px;color:var(--ink-soft);text-align:justify}
.entry{margin-top:11px;overflow:hidden}
.entry + .entry{margin-top:23px}
.feed{margin-top:17px;overflow:hidden}
.feed + .feed{margin-top:11px}
.feed .avatar{width:54px;height:52px;border:1px solid #ddd;float:left;margin-right:10px}
.feed h3{font-size:13px;font-weight:400;color:var(--heading-blue);margin-bottom:3px}
.pill-blue{color:#8fd1f5;position:absolute;top:940px}

/* footer */
.site-footer{left:0;top:994px;width:1050px;height:106px;background:var(--footer-bg)}
.footer-links{left:44px;top:1022px;font-size:13px;color:var(--footer-text)}
.footer-links span{margin:0 9px;color:#aaa}
.copyright{left:44px;top:1057px;font-size:13px;color:var(--footer-text)}
.social{top:1035px;width:22px;height:22px;border-radius:3px}
</style>
</head>
<body>
<div class="page">

  <header class="site-header abs"></header>
  <div class="brand abs"><span class="brand-mark"></span><span class="brand-name">Vitor Bis</span></div>
  <svg class="nav-marker abs" width="34" height="18" viewBox="0 0 34 18"><path d="M0 0h34L17 17z" fill="#b8d630"/></svg>
  <nav class="main-nav abs">
    <a class="current">Home</a><a>About Us</a><a>Contact Us</a><a>Log in</a>
  </nav>

  <section class="hero abs"></section>
  <svg class="hero-sweep abs" width="1050" height="430" viewBox="0 0 1050 430">
    <path d="M0 60 C250 120 420 140 700 0" stroke="rgba(255,255,255,.18)" stroke-width="2" fill="none"/>
    <path d="M0 310 C300 260 700 380 1050 330" stroke="rgba(255,255,255,.16)" stroke-width="2" fill="none"/>
    <path d="M200 0 C380 90 470 160 500 260" stroke="rgba(255,255,255,.12)" stroke-width="3" fill="none"/>
  </svg>
  <p class="hero-pitch abs">Are you a nurse, personal trainer or health science student? Use vitorbis.com as a database of your patients, for studies or simply to evaluate your techniques. <a>View more...</a></p>
  <div class="btn btn-signup abs">Sign Up for free</div>
  <div class="btn btn-login abs">Log in</div>
  <p class="hero-tagline abs">The ultimate platform for health care professionals and patients to meet in the cloud.</p>
  <div class="photo-frame abs"></div>
  <div class="photo-slot abs" role="img" aria-label="Smiling team of medical staff in white coats"></div>
  <div class="slider-controls abs">
    <span>« Previous</span>
    <span class="dot active"></span><span class="dot"></span><span class="dot"></span><span class="dot"></span><span class="dot"></span>
    <span>Next »</span>
  </div>

  <section class="welcome abs"></section>
  <h1 class="welcome-title abs" style="font-weight:400">Welcome to our site</h1>
  <p class="welcome-text abs">Ut enim ad minim veniam, quis nostrud exercitation ullamco laboris nisi ut aliquip ex ea commodo consequat. Duis aute irure dolor in reprehenderit in voluptate velit esse cillum dolore eu fugiat nulla pariatur. <span class="pill pill-green">View more</span></p>

  <section class="col abs" style="left:65px">
    <h2>About Us</h2>
    <div class="entry">
      <div class="thumb" role="img" aria-label="Doctor speaking with an elderly patient" style="background:linear-gradient(135deg,#dfe6ea,#b9c4cc)"></div>
      <p class="body-copy">Duis aute irure dolor in repre­henderit in voluptate velit esse cillum dolore eu fugiat nulla pariatur.</p>
    </div>
    <p class="body-copy" style="margin-top:8px">Sed ut perspiciatis unde omnis iste natus error sit voluptatem accusantium doloremque laudantium, totam rem aperiam, eaque ipsa quae ab illo inven­tore veritatis et quasi architecto beatae vitae dicta sunt explicabo. Nemo enim ipsam voluptatem quia voluptas sit aspernatur aut odit aut fugit</p>
  </section>
  <span class="pill pill-blue" style="left:237px">View more</span>

  <section class="col abs" style="left:401px">
    <h2>Advertising</h2>
    <div class="entry">
      <div class="thumb" role="img" aria-label="Hand holding a stethoscope" style="background:linear-gradient(135deg,#eef0f0,#c9d0d4)"></div>
      <p class="body-copy">Duis aute irure dolor in repre­henderit in voluptate velit esse cillum dolore eu fugiat nulla pariatur.</p>
    </div>
    <div class="entry">
      <div class="thumb" role="img" aria-label="Nurse in scrubs holding a clipboard" style="background:linear-gradient(135deg,#5c8d86,#2f5f5a)"></div>
      <p class="body-copy">Duis aute irure dolor in repre­henderit in voluptate velit esse cillum dolore eu fugiat nulla pariatur.</p>
    </div>
  </section>
  <span class="pill pill-blue" style="left:573px">View more</span>

  <section class="col abs" style="left:737px">
    <h2>Chirpline Feeds</h2>
    <div class="feed">
      <div class="avatar" role="img" aria-label="Profile photo of a doctor" style="background:linear-gradient(#e8eef2,#c5d0d8)"></div>
      <h3>Nostrud exercitation ullamco</h3>
      <p class="body-copy">Duis aute irure dolor in reprehenderit in voluptate velit esse cillum dolore eu fugiat nulla pariatur.</p>
    </div>
    <div class="feed">
      <div class="avatar" role="img" aria-label="Profile photo of a woman" style="background:linear-gradient(#eeeae0,#c9c4a8)"></div>
      <h3>Nostrud exercitation ullamco</h3>
      <p class="body-copy">Duis aute irure dolor in reprehenderit in voluptate velit esse cillum dolore eu fugiat nulla pariatur.</p>
    </div>
    <div class="feed">
      <div class="avatar" role="img" aria-label="Empty profile placeholder" style="background:#d4d4d4"></div>
      <h3>Nostrud exercitation ullamco</h3>
      <p class="body-copy">Duis aute irure dolor in reprehenderit in voluptate velit esse cillum dolore eu fugiat nulla pariatur.</p>
    </div>
  </section>

  <footer class="site-footer abs"></footer>
  <p class="footer-links abs">Home<span>|</span>About Us<span>|</span>Contact us<span>|</span>Login<span>|</span>Sitemap</p>
  <p class="copyright abs">Copyright © 2011 www.vitorbis.com &nbsp; All rights reserved</p>
  <span class="social abs" style="left:827px;background:#3b5998" aria-label="Social profile"></span>
  <span class="social abs" style="left:867px;background:#4fb6e8" aria-label="Social profile"></span>
  <span class="social abs" style="left:907px;background:#f57d00" aria-label="Social profile"></span>
  <span class="social abs" style="left:947px;background:#1c75ad" aria-label="Social profile"></span>
  <span class="social abs" style="left:987px;background:#4a9d3a" aria-label="Social profile"></span>

</div>
</body>
</html>
```